Billboard design for dentist that sees only children

I own a 12' x 25' digital billboard and I need help with billboard design. My wife is a general dentist that only sees children and is very passionate about giving them a quality dental experience . She has a great reputation in town. Obviously with a billboard there can't be a lot of reading. Maybe something that shows safety, love, experience and children. I am completely open to your ideas. In addition I have other businesses that also need billboard design so this could lead to more work. If you go to Maplecovedental.com under the about section you will find more information about the practice and our phone number. Attached is our logo which could be changed and content specs for the digital billboard. Happy Designing!!

Target Market(s)

Parents with children

Colors

Designer to choose colors to be used in the design.

Requirements
Must have
• Must attract attention and be nice to look at.
Nice to have
• Probably should have children in the picture ..... Maybe
Should not have
• If I see something I don't like I will let you know

```html
<!DOCTYPE html>
<html lang="en">
<head>
<meta charset="utf-8">
<title>Maple Cove Dental – Billboard</title>
<link href="https://fonts.googleapis.com/css2?family=Pacifico&family=Roboto+Condensed:ital,wght@0,300;0,400;0,700;1,300&display=swap" rel="stylesheet">
<style>
  :root {
    --page-bg: #e6e8eb;
    --board-white: #ffffff;
    --brand-teal: #2f7d6e;
    --brand-green: #3aa58a;
    --brand-blue: #27a4dd;
    --deep-ink: #1d2b2a;
    --band-dark: #222628;
    --text-white: #ffffff;
  }
  * { margin: 0; padding: 0; box-sizing: border-box; }
  html, body {
    width: 1200px; height: 794px; overflow: hidden;
    background: var(--page-bg);
  }
  .billboard {
    position: absolute; left: 0; top: 109px;
    width: 1200px; height: 576px;
    background: var(--board-white);
    overflow: hidden;
    font-family: "Roboto Condensed", Arial, sans-serif;
  }
  .artwork { position: absolute; inset: 0; }

  .brand { position: absolute; left: 36px; top: 34px; display: flex; align-items: center; gap: 14px; }
  .brand-dot { width: 56px; height: 56px; border-radius: 50%; background: var(--brand-teal); }
  .brand-name { font-size: 50px; font-weight: 400; color: var(--brand-teal); line-height: 1; }
  .brand-tagline {
    position: absolute; left: 226px; top: 92px;
    font-size: 22px; font-weight: 300; font-style: italic; color: var(--brand-blue);
  }

  .headline { position: absolute; left: 36px; top: 140px; }
  .headline-small {
    position: absolute; left: 0; top: 82px;
    font-size: 34px; font-weight: 400; color: var(--brand-teal); line-height: 0.95;
    white-space: nowrap;
  }
  .headline-script {
    position: absolute; left: 158px; top: 0;
    font-family: "Pacifico", cursive; font-size: 118px; color: var(--brand-blue); line-height: 1;
    white-space: nowrap;
  }

  .promise { position: absolute; left: 36px; top: 338px; text-transform: uppercase; white-space: nowrap; }
  .promise-lead { font-size: 28px; font-weight: 400; color: var(--deep-ink); padding-left: 22px; }
  .promise-main { font-size: 60px; font-weight: 700; color: var(--brand-blue); line-height: 1; }

  .contact-phone {
    position: absolute; left: 0; top: 448px; width: 560px; height: 62px;
    background: var(--brand-blue); display: flex; align-items: center; padding-left: 30px; gap: 16px;
    color: var(--text-white); font-size: 52px; font-weight: 700;
  }
  .contact-info {
    position: absolute; left: 0; top: 510px; width: 560px; height: 66px;
    background: var(--band-dark); padding: 8px 0 0 30px;
    color: var(--text-white); font-size: 20px; line-height: 26px;
  }
  .contact-row { display: flex; align-items: center; gap: 10px; }
</style>
</head>
<body>
  <main class="billboard">
    <svg class="artwork" width="1200" height="576" viewBox="0 0 1200 576">
      <defs>
        <linearGradient id="kids-photo-tone" x1="0" y1="0" x2="0.3" y2="1">
          <stop offset="0" stop-color="#e4eef5"/>
          <stop offset="0.3" stop-color="#e2c2ab"/>
          <stop offset="0.6" stop-color="#c98a72"/>
          <stop offset="0.85" stop-color="#b8625f"/>
          <stop offset="1" stop-color="#e08a95"/>
        </linearGradient>
        <linearGradient id="brushing-photo-tone" x1="0" y1="0" x2="1" y2="1">
          <stop offset="0" stop-color="#f4f1ec"/>
          <stop offset="0.6" stop-color="#e7bfa4"/>
          <stop offset="1" stop-color="#d8a07f"/>
        </linearGradient>
      </defs>
      <path class="photo-frame" d="M586 0 Q496 240 578 430 L680 576 H1200 V0 Z" fill="var(--brand-green)"/>
      <g role="img" aria-label="Photo of a group of smiling children">
        <path d="M606 0 Q520 240 598 424 L700 576 H1200 V0 Z" fill="url(#kids-photo-tone)"/>
      </g>
      <path class="photo-wave" d="M720 576 Q980 548 1200 452 V576 Z" fill="var(--brand-teal)"/>
      <circle cx="624" cy="466" r="114" fill="var(--brand-blue)"/>
      <circle cx="624" cy="466" r="106" fill="var(--brand-teal)"/>
      <g role="img" aria-label="Photo of a mother brushing a toddler's teeth">
        <circle cx="624" cy="466" r="98" fill="url(#brushing-photo-tone)"/>
      </g>
      <path class="smile-curve" d="M330 262 Q400 298 478 254 Q400 286 330 262 Z" fill="var(--deep-ink)"/>
    </svg>

    <div class="brand">
      <span class="brand-dot"></span>
      <span class="brand-name">Maple Cove Dental</span>
    </div>
    <div class="brand-tagline">general dentistry for children</div>

    <div class="headline">
      <div class="headline-small">HEALTHY<br>BEAUTIFUL</div>
      <div class="headline-script">Smile</div>
    </div>

    <div class="promise">
      <div class="promise-lead">We bring back smiles to</div>
      <div class="promise-main">Your kids life</div>
    </div>

    <div class="contact-phone">
      <svg width="40" height="40" viewBox="0 0 40 40" aria-hidden="true">
        <circle cx="20" cy="20" r="19" fill="var(--text-white)"/>
        <path d="M14 10 l4 6 -2 3 q2 4 6 6 l3 -2 6 4 -2 4 q-10 0 -17 -10 q-3 -6 0 -10 z" fill="var(--brand-blue)"/>
      </svg>
      <span>555 014 2387</span>
    </div>

    <div class="contact-info">
      <div class="contact-row">
        <svg width="14" height="18" viewBox="0 0 14 18" aria-hidden="true">
          <path d="M7 0 a7 7 0 0 1 7 7 c0 5 -7 11 -7 11 s-7 -6 -7 -11 a7 7 0 0 1 7 -7 z" fill="var(--brand-blue)"/>
          <circle cx="7" cy="7" r="2.6" fill="var(--band-dark)"/>
        </svg>
        <span>428 Harbor Lane Ridgefield, NM 88000</span>
      </div>
      <div class="contact-row">
        <svg width="14" height="14" viewBox="0 0 14 14" aria-hidden="true">
          <circle cx="7" cy="7" r="6" fill="none" stroke="var(--brand-blue)" stroke-width="2"/>
          <path d="M1 7 H13 M7 1 Q3 7 7 13 M7 1 Q11 7 7 13" fill="none" stroke="var(--brand-blue)" stroke-width="1.2"/>
        </svg>
        <span>www.maplecovedental.com</span>
      </div>
    </div>
  </main>
</body>
</html>
```